Professional business cards for real estate development company

I need business cards for my new real estate development company. The company, "KORVA" is a real estate development, investment, and advisory firm with a focus on multifamily, office, and mixed-use projects across primary and secondary markets in the Southeast United States.

Style preference is modern

Industry/Entity Type

Real Estate Development

Contact Information for Business Card

The business cards need to include:
Name
Title
Mailing Address
Phone Number
Web Address

Logo is attached. I would like white to be the primary color with incorporation of the company colors: #232D3A and #B5A451

Font styles to use
Other font styles liked:
• Montserrat, Avenir

Requirements
Must have
• Company Logo. No need to include the company name since the name is in the logo.
Should not have
• No line type designs

```html
<!DOCTYPE html>
<html lang="en">
<head>
<meta charset="utf-8">
<title>KORVA Business Card</title>
<link rel="stylesheet" href="https://fonts.googleapis.com/css2?family=Montserrat:wght@400;500;600&display=swap">
<style>
  :root {
    --navy: #232d3a;
    --gold: #b5a451;
    --paper: #f9f9f9;
    --page: #ffffff;
  }
  * { margin: 0; padding: 0; box-sizing: border-box; }
  html, body {
    width: 783px;
    height: 1200px;
    overflow: hidden;
    background: var(--page);
    font-family: "Montserrat", sans-serif;
  }
  .sheet {
    position: relative;
    width: 783px;
    height: 1200px;
  }
  .card {
    position: absolute;
    top: 126px;
    width: 300px;
    height: 183px;
  }
  .card--front {
    left: 66px;
    background: var(--navy);
    display: flex;
    align-items: center;
    justify-content: center;
  }
  .brand-name {
    color: var(--gold);
    font-weight: 500;
    font-size: 22px;
    letter-spacing: 3px;
    display: flex;
    align-items: center;
    gap: 8px;
  }
  .brand-mark {
    width: 9px;
    height: 9px;
    background: var(--gold);
  }
  .card--back {
    left: 418px;
    background: var(--paper);
    color: var(--navy);
  }
  .holder-name {
    position: absolute;
    left: 38px;
    top: 32px;
    font-size: 11.5px;
    font-weight: 600;
  }
  .holder-title {
    position: absolute;
    left: 38px;
    top: 50px;
    font-size: 8px;
    letter-spacing: 1.8px;
  }
  .contact-list {
    position: absolute;
    left: 20px;
    top: 84px;
    list-style: none;
  }
  .contact-item {
    display: flex;
    align-items: flex-start;
    gap: 7px;
    font-size: 7.8px;
    line-height: 11px;
    margin-bottom: 7.5px;
  }
  .contact-bullet {
    flex: none;
    width: 11px;
    height: 11px;
    background: var(--navy);
  }
</style>
</head>
<body>
  <main class="sheet">
    <section class="card card--front">
      <div class="brand-name"><span class="brand-mark"></span>KORVA</div>
    </section>
    <section class="card card--back">
      <h1 class="holder-name">Anika Deshmane</h1>
      <p class="holder-title">DESIGNATION</p>
      <ul class="contact-list">
        <li class="contact-item"><span class="contact-bullet"></span><span>+914055512098</span></li>
        <li class="contact-item"><span class="contact-bullet"></span><span>lorem.ipsum@lorem.com</span></li>
        <li class="contact-item"><span class="contact-bullet"></span><span>www.loremipsum.com</span></li>
        <li class="contact-item"><span class="contact-bullet"></span><span>Lorem Ipsum, Dummy text<br>ipsum industry 123456</span></li>
      </ul>
    </section>
  </main>
</body>
</html>
```